Business card design for a dynamic IT consulting company

We need a business card design for a young firm, specialized in the Telecommunications/Consulting industry. The name of the company is Brask and Partners Business Consulting Ltd. (Short name: Brask and Partnes)
Brask = solve read reverse, so we aim to be uncomplicated and solution-oriented. The small pipe in our logo is also related to the word solve. So we need a new business card design, which is simple, eye catching and something non traditional (I would probably prefer a square shaped design rather than a rectangle, but open for suggestions). Attached our logo.

Target Market(s)

Usually our customers are Tier1 Telecoms providers (Q-Linkra, Parnexo, etc) and their executives.

Industry/Entity Type

Business

Contact Information for Business Card

Name: Gergely Halmindo
Email: g.halmindo@braskpartnera.hu
Web: www.braskpartnera.hu
Mobile: +36 30 555 0192
Title: Managing Director

Optional:
Company name: Brask and Partners Ltd.
Address: 1047 Budapest, Ravaszi str. 17/B, Hungary

Font styles to use
Other font styles liked:
• helveticaneue_medium, Prime Regular are used now.

Colors

Designer to choose colors to be used in the design.

Requirements
Must have
• I would like to have a 2 sided design.
Nice to have
• I thought if we make the logo a bit bigger (without the company name), that could go to the back with the company name below. I though, if the pipe in the logo is somehow touchable on the business card, would be nice and unique.

```html
<!DOCTYPE html>
<html lang="en">
<head>
<meta charset="utf-8">
<title>Brask and Partners – Business Card</title>
<link rel="stylesheet" href="https://fonts.googleapis.com/css2?family=Source+Sans+3:wght@400;600;700&display=swap">
<style>
  :root {
    --backdrop: #262626;
    --kraft-light: #cfae85;
    --kraft-mid: #c09a6d;
    --kraft-dark: #a9825a;
    --ink: #2a231b;
    --ink-soft: #3a3026;
  }
  * { margin: 0; padding: 0; box-sizing: border-box; }
  html, body {
    width: 1200px; height: 900px; overflow: hidden;
    background: var(--backdrop);
    font-family: "Source Sans 3", "Myriad Pro", Arial, sans-serif;
    color: var(--ink);
  }
  .stage { position: relative; width: 1200px; height: 900px; }
  .card {
    position: absolute; top: 306px;
    width: 440px; height: 271px;
    background: linear-gradient(155deg, var(--kraft-light) 0%, var(--kraft-mid) 55%, var(--kraft-dark) 100%);
  }
  .card--front { left: 149px; }
  .card--back { left: 608px; }

  .brand {
    position: absolute; display: flex; align-items: center; gap: 12px;
    font-weight: 400; color: var(--ink); white-space: nowrap; line-height: 1;
  }
  .brand__square { width: 30px; height: 30px; background: var(--ink); }
  .brand__name { font-size: 38px; letter-spacing: 0.5px; }
  .card--front .brand { left: 40px; top: 64px; }
  .card--back .brand { left: 40px; top: 113px; }

  .person {
    position: absolute; right: 237px; top: 166px; text-align: right;
  }
  .person__name { font-size: 14.5px; font-weight: 700; line-height: 17px; }
  .person__title { font-size: 12px; font-weight: 400; color: var(--ink-soft); line-height: 16px; }

  .divider {
    position: absolute; left: 220px; top: 141px;
    width: 1px; height: 81px; background: var(--ink-soft);
  }

  .contacts { position: absolute; left: 235px; top: 141px; list-style: none; }
  .contacts li {
    display: flex; align-items: center; gap: 8px;
    font-size: 13px; line-height: 14.7px;
  }
  .contacts svg { width: 8px; height: 8px; fill: var(--ink); flex: none; }

  .address {
    position: absolute; left: 234px; top: 195px;
    font-size: 12px; font-weight: 600; line-height: 15.7px; font-style: normal;
  }
</style>
</head>
<body>
<main class="stage">
  <section class="card card--front" aria-label="Business card front">
    <div class="brand">
      <span class="brand__square"></span>
      <span class="brand__name">Brask &amp; Partners</span>
    </div>

    <div class="person">
      <p class="person__name">Gergely Halmindo</p>
      <p class="person__title">Managing Director</p>
    </div>

    <span class="divider"></span>

    <ul class="contacts">
      <li>
        <svg viewBox="0 0 8 8" aria-hidden="true"><path d="M2 0h4a1 1 0 0 1 1 1v6a1 1 0 0 1-1 1H2a1 1 0 0 1-1-1V1a1 1 0 0 1 1-1zm0 1v5h4V1z"/></svg>
        +36 30 555 0192
      </li>
      <li>
        <svg viewBox="0 0 8 8" aria-hidden="true"><path d="M0 1.5h8v5H0zM.6 2l3.4 2.4L7.4 2z" fill-rule="evenodd"/></svg>
        g.halmindo@braskpartnera.hu
      </li>
      <li>
        <svg viewBox="0 0 8 8" aria-hidden="true"><circle cx="4" cy="4" r="4"/></svg>
        www.braskpartnera.hu
      </li>
    </ul>

    <address class="address">
      Brask and Partners Ltd.<br>
      1047 Budapest, Ravaszi str.<br>
      17/B, Hungary
    </address>
  </section>

  <section class="card card--back" aria-label="Business card back">
    <div class="brand">
      <span class="brand__square"></span>
      <span class="brand__name">Brask &amp; Partners</span>
    </div>
  </section>
</main>
</body>
</html>
```